Quellmont Digital - WebSite Design and Hosting

Emphasis on Quellmont Digital Website Development

Prioritize the development of the website for "quellmontdigital.example" as the first and foremost project.

Client-Friendly Website Request Process
** Design the website to facilitate easy interaction for small and medium-sized business (SMB) customers who require a website.
** Include a user-friendly form that allows my customers to submit their website requirements. This form should enable customers to:
** They can Upload images and logos related to their brand.
** They can Select brand colors that align with their identity.

Provide ample space for them to add extensive information about their business and services.

Extensive Portfolio Showcase
Build a portfolio section featuring a minimum of 300 website examples. These examples should be categorized and presented in a way that makes it convenient for potential clients to sort through and select as references for their own projects.

Summary:
In summary, the primary focus is on developing "quellmontdigital.example" as the initial project. The website should be user-friendly for SMB clients, offering a form for submitting detailed requirements, including image and logo uploads and brand color selection. Additionally, an extensive portfolio with 300 website examples should be presented for clients' reference and convenience.

Target Market(s)

Small Business Owners who need a local website

Industry/Entity Type

WebDesign and hosting (A marketing agency)

Coding

Coded - Design and coding required

Number of Pages Required

5+ page

Font styles to use
Sans Serif
Script

Colors
0054AA
0677BA
7BADD7
CADEEF
E8F1F8
FFF300
FFF600
FEFA6F
FFFEC7
FFFEE8

Requirements
Must have
• Black background! My customers need a form to pick a website design package, upload logo, brand colors and description. That input must be easy to submit to Pixel Harbor to do the ProJet, we will add marketing services as well
Nice to have
• Step by step like explanaining to a 5th grader what the instructions are to get signed up. I want high tech state of the art - for SMB owners who may not be tech savvy

```html
<!DOCTYPE html>
<html lang="en">
<head>
<meta charset="utf-8">
<title>Quellmont Digital</title>
<link rel="stylesheet" href="https://fonts.googleapis.com/css2?family=Abril+Fatface&family=Montserrat:wght@400;500;600;700&display=swap">
<style>
:root{
  --green:#13a352;
  --ink:#111111;
  --charcoal:#333333;
  --white:#ffffff;
  --line:#d6d6d6;
  --display:"Abril Fatface", serif;
  --text:"Montserrat", sans-serif;
}
*{box-sizing:border-box;margin:0;padding:0}
html,body{width:1200px;height:3193px;overflow:hidden;background:var(--white);font-family:var(--text);color:var(--ink)}
.page{position:relative;width:1200px;height:3193px}
.abs{position:absolute}
.shape{position:absolute;left:0;top:0}

/* header */
.brand{left:174px;top:18px;font-family:var(--display);font-size:44px;color:var(--ink);letter-spacing:.3px}
.btn{position:absolute;display:flex;align-items:center;justify-content:center;border-radius:22px;font-weight:600;font-size:19px;color:var(--white)}
.btn-signup{left:714px;top:25px;width:108px;height:38px;background:var(--green)}
.btn-start{left:831px;top:25px;width:145px;height:38px;background:var(--charcoal)}
.menu{left:991px;top:34px;width:37px}
.menu span{display:block;height:3px;background:var(--ink);margin-bottom:7px;border-radius:2px}

/* shared */
.display-title{position:absolute;left:0;width:1200px;text-align:center;font-family:var(--display);font-size:54px}
.display-title .accent{color:var(--green)}
.badge{position:absolute;width:132px;height:132px;border-radius:50%;background:var(--white);border:7px solid var(--green);display:flex;align-items:center;justify-content:center;font-family:var(--display);font-size:82px;color:var(--green);line-height:1;padding-top:4px}

/* hero */
.hero-title{top:212px;color:var(--white);font-size:62px}
.dots{left:571px;top:588px;display:flex;gap:10px}
.dots span{width:13px;height:13px;border-radius:50%;background:#8e8e8e}
.dots span:first-child{background:var(--white)}
.divider{left:65px;top:739px;width:1071px;height:1px;background:#eeeeee}

/* templates */
.template{position:absolute;top:780px;width:272px;height:460px;background:var(--white);border:1px solid #cfcfcf;box-shadow:0 2px 10px rgba(0,0,0,.25);padding:5px}
.template .shot{width:100%;height:100%}
.shot-dark{background:linear-gradient(180deg,#1c1c1c 0%,#3a3a3a 28%,#f1f1f1 30%,#e9e9e9 64%,#2a2a2a 66%,#f4f4e8 100%)}
.shot-blue{background:linear-gradient(180deg,#24408c 0%,#3d6bc4 31%,#f7f7f5 33%,#eeeeea 55%,#2e5aa6 57%,#dfe6ef 74%,#f7f7f5 76%,#f2f2ef 100%)}
.shot-warm{background:linear-gradient(180deg,#d9c9b4 0%,#b98a5e 31%,#ffffff 33%,#f3ece4 55%,#fafafa 57%,#ffffff 73%,#e8923a 76%,#f7f2ec 100%)}
.chev{position:absolute;top:996px;width:30px;height:48px}
.more{position:absolute;top:1269px;width:174px;height:43px;border:2px solid var(--ink);border-radius:22px;display:flex;align-items:center;justify-content:center;font-size:15.5px;font-weight:500;background:var(--white)}
.more.is-active{background:var(--green);border-color:var(--green);color:var(--white);font-weight:600}

/* plans */
.plan-title{top:1482px;color:var(--white)}
.plan-copy{left:173px;top:1637px;width:452px;color:var(--white);font-size:18.2px;line-height:27px;text-align:justify;font-weight:500}
.plan-copy p+p{margin-top:16px}
.signup-card{left:679px;top:1596px;width:349px;height:333px;background:var(--white);border-radius:38px 30px 30px 38px;padding:10px 11px}
.signup-card h3{text-align:center;font-size:40px;font-weight:600;margin-top:4px;margin-bottom:14px}
.field{height:42px;border:2px solid var(--ink);border-radius:22px;display:flex;align-items:center;padding-left:13px;font-size:16.5px;font-weight:500;margin-bottom:11px}
.submit{width:111px;height:41px;background:var(--green);color:var(--white);border-radius:21px;display:flex;align-items:center;justify-content:center;font-size:19px;font-weight:600;margin-top:8px}

/* testimonials */
.clients-title{top:2152px}
.client{position:absolute;top:2264px;width:250px;text-align:center}
.avatar{width:188px;height:188px;border-radius:50%;border:3px solid var(--green);margin:0 auto}
.av1{background:radial-gradient(circle at 50% 45%,#6b4a3a 0%,#2c2f3a 55%,#7a7062 100%)}
.av2{background:radial-gradient(circle at 50% 45%,#e6cfa2 0%,#bdbdbd 50%,#f1f1f1 100%)}
.av3{background:radial-gradient(circle at 50% 45%,#4b3226 0%,#9fb0c4 55%,#d9a23a 100%)}
.av4{background:radial-gradient(circle at 50% 45%,#c39a82 0%,#8ea26a 55%,#dfe6d0 100%)}
.client h4{font-size:22.5px;font-weight:600;margin-top:14px}
.client p{font-size:15.8px;line-height:19.5px;font-weight:500;margin-top:6px}
.client .role{font-size:15.5px;margin-top:10px}

/* footer */
.foot-brand{right:172px;top:2756px;font-family:var(--display);font-size:62px;color:var(--white)}
.foot-col{position:absolute;top:2897px;color:var(--white)}
.foot-col h5{font-size:24px;font-weight:500;margin-bottom:13px}
.links li{list-style:none;font-size:19px;font-weight:500;line-height:25.7px}
.contact-item{display:flex;gap:9px;font-size:19px;font-weight:500;line-height:25px;align-items:flex-start}
.contact-item svg{flex:none;margin-top:6px}
.touch p{width:305px;font-size:14.5px;line-height:21px;text-align:justify;font-weight:500}
.foot-rule{left:173px;top:3126px;width:855px;height:1px;background:#8a8a8a}
.copyright{left:0;top:3158px;width:1200px;text-align:center;color:var(--white);font-size:14.5px;font-weight:500}
</style>
</head>
<body>
<div class="page">

  <!-- header -->
  <div class="abs brand">QuellmontDigital</div>
  <div class="btn btn-signup">Sign Up</div>
  <div class="btn btn-start">Get Started</div>
  <div class="abs menu"><span></span><span></span><span></span></div>

  <!-- hero -->
  <svg class="shape" width="1200" height="760" viewBox="0 0 1200 760" role="img" aria-label="Photo of a team of young professionals gathered around a laptop in an office, darkened">
    <defs>
      <linearGradient id="heroFill" x1="0" y1="0" x2="1" y2="1">
        <stop offset="0" stop-color="#5a5a58"/>
        <stop offset=".45" stop-color="#3a3733"/>
        <stop offset=".8" stop-color="#1e1d1b"/>
        <stop offset="1" stop-color="#0c0c0c"/>
      </linearGradient>
    </defs>
    <path d="M65,82 H1136 V470 C1136,560 1090,620 1010,620 H260 C150,620 85,680 65,739 Z" fill="url(#heroFill)"/>
  </svg>
  <div class="display-title hero-title">QuellmontDigital</div>
  <div class="abs dots"><span></span><span></span><span></span></div>
  <div class="badge" style="left:967px;top:524px">01</div>
  <svg class="shape" width="1200" height="760" viewBox="0 0 1200 760">
    <path d="M948,656 C944,690 905,712 855,712" fill="none" stroke="#111" stroke-width="3" stroke-dasharray="9 7"/>
    <path d="M868,702 L851,712 L868,722" fill="none" stroke="#111" stroke-width="3" stroke-linecap="round" stroke-linejoin="round"/>
  </svg>
  <div class="abs divider"></div>

  <!-- templates -->
  <div class="display-title" style="top:676px">Review <span class="accent">Templates</span></div>

  <svg class="chev" style="left:68px" viewBox="0 0 30 48"><path d="M26,2 L4,24 L26,46" fill="none" stroke="#111" stroke-width="2.5"/></svg>
  <svg class="chev" style="left:1103px" viewBox="0 0 30 48"><path d="M4,2 L26,24 L4,46" fill="none" stroke="#111" stroke-width="2.5"/></svg>

  <div class="template" style="left:174px"><div class="shot shot-dark" role="img" aria-label="Template preview: dark data protection website with yellow accents"></div></div>
  <div class="template" style="left:465px"><div class="shot shot-blue" role="img" aria-label="Template preview: blue corporate consulting website"></div></div>
  <div class="template" style="left:756px"><div class="shot shot-warm" role="img" aria-label="Template preview: light business coaching website with orange accents"></div></div>

  <div class="more" style="left:223px">View More Details</div>
  <div class="more is-active" style="left:515px">View More Details</div>
  <div class="more" style="left:806px">View More Details</div>

  <!-- plans -->
  <svg class="shape" style="top:1300px" width="1200" height="940" viewBox="0 1300 1200 940" role="img" aria-label="Photo of business people meeting around a conference table, darkened">
    <defs>
      <linearGradient id="planFill" x1="0" y1="0" x2="1" y2="1">
        <stop offset="0" stop-color="#2a2a28"/>
        <stop offset=".5" stop-color="#3d3c38"/>
        <stop offset="1" stop-color="#1a1a19"/>
      </linearGradient>
    </defs>
    <path d="M1136,1326 V1940 C1136,2020 1090,2096 1010,2096 H250 C140,2096 80,2160 65,2213 V1600 C65,1510 130,1443 240,1443 H960 C1060,1443 1120,1390 1136,1326 Z" fill="url(#planFill)"/>
  </svg>
  <div class="badge" style="left:103px;top:1397px">02</div>
  <svg class="shape" style="top:1500px" width="400" height="110" viewBox="0 1500 400 110">
    <path d="M232,1530 C230,1565 265,1590 328,1587" fill="none" stroke="#fff" stroke-width="3" stroke-dasharray="9 7"/>
    <path d="M318,1577 L332,1587 L318,1597" fill="none" stroke="#fff" stroke-width="3" stroke-linecap="round" stroke-linejoin="round"/>
  </svg>
  <div class="display-title plan-title">Sign Up for a Plan</div>

  <div class="abs plan-copy">
    <p>Duis aute irure dolor in reprehenderit in voluptate velit esse cillum dolore eu fugiat nulla pariatur. Excep teur sint occaecat cupidatat non proident.</p>
    <p>Nemo enim ipsam voluptatem quia voluptas sit asper natur aut odit aut fugit, sed quia consequuntur magni dolores eos qui ratione voluptatem sequi nesciunt. Neque porro quisquam est, qui dolorem ipsum quia dolor sit amet, consectetur, adipisci velit, sed quia non numquam eius modi tempora incidunt.</p>
  </div>

  <div class="abs signup-card">
    <h3>Sign Up</h3>
    <div class="field">Name</div>
    <div class="field">Email Address</div>
    <div class="field">Password</div>
    <div class="submit">Submit</div>
  </div>

  <div class="badge" style="left:967px;top:2002px">03</div>
  <svg class="shape" style="top:2120px" width="1200" height="90" viewBox="0 2120 1200 90">
    <path d="M948,2134 C944,2168 905,2188 855,2188" fill="none" stroke="#111" stroke-width="3" stroke-dasharray="9 7"/>
    <path d="M868,2178 L851,2188 L868,2198" fill="none" stroke="#111" stroke-width="3" stroke-linecap="round" stroke-linejoin="round"/>
  </svg>

  <!-- testimonials -->
  <div class="display-title clients-title">What <span class="accent">Clients Say!</span></div>

  <div class="client" style="left:100px">
    <div class="avatar av1" role="img" aria-label="Portrait of a smiling businesswoman in a dark suit"></div>
    <h4>Marisol Keating</h4>
    <p>Nemo enim ipsam voluptatem quia voluptas sit aspernatur aut odit aut fugit, sed quia con sequuntur magnis</p>
    <div class="role">- Head Of Team</div>
  </div>
  <div class="client" style="left:348px">
    <div class="avatar av2" role="img" aria-label="Portrait of a smiling blonde woman with glasses"></div>
    <h4>Tessa Wrenfield</h4>
    <p>Nemo enim ipsam voluptatem quia voluptas sit aspernatur aut odit aut fugit, sed quia con sequuntur magnis</p>
    <div class="role">- Head Of Team</div>
  </div>
  <div class="client" style="left:604px">
    <div class="avatar av3" role="img" aria-label="Portrait of a smiling man in a light grey suit"></div>
    <h4>Idris Calloway</h4>
    <p>Nemo enim ipsam voluptatem quia voluptas sit aspernatur aut odit aut fugit, sed quia con sequuntur magnis</p>
    <div class="role">- Head Of Team</div>
  </div>
  <div class="client" style="left:851px">
    <div class="avatar av4" role="img" aria-label="Portrait of a smiling man with glasses and a tie"></div>
    <h4>Gregor Ashdown</h4>
    <p>Nemo enim ipsam voluptatem quia voluptas sit aspernatur aut odit aut fugit, sed quia con sequuntur magnis</p>
    <div class="role">- Head Of Team</div>
  </div>

  <!-- footer -->
  <svg class="shape" style="top:2590px" width="1200" height="603" viewBox="0 2590 1200 603">
    <path d="M1136,2596 V3193 H65 V2880 C65,2780 130,2714 240,2714 H960 C1060,2714 1120,2660 1136,2596 Z" fill="#000"/>
  </svg>
  <div class="badge" style="left:103px;top:2670px">04</div>
  <svg class="shape" style="top:2790px" width="400" height="80" viewBox="0 2790 400 80">
    <path d="M232,2801 C230,2836 265,2860 328,2857" fill="none" stroke="#fff" stroke-width="3" stroke-dasharray="9 7"/>
    <path d="M318,2847 L332,2857 L318,2867" fill="none" stroke="#fff" stroke-width="3" stroke-linecap="round" stroke-linejoin="round"/>
  </svg>
  <div class="abs foot-brand">QuellmontDigital</div>

  <div class="foot-col" style="left:173px">
    <h5>Quick Links</h5>
    <ul class="links">
      <li>Home</li><li>About Us</li><li>Pricing Plans</li><li>Services</li><li>Blog</li><li>Templates</li>
    </ul>
  </div>

  <div class="foot-col" style="left:390px">
    <h5>Contact Us</h5>
    <div class="contact-item" style="margin-top:18px">
      <svg width="15" height="15" viewBox="0 0 24 24"><path d="M5 2h4l2 5-3 2a12 12 0 0 0 7 7l2-3 5 2v4a2 2 0 0 1-2 2A18 18 0 0 1 3 4a2 2 0 0 1 2-2z" fill="none" stroke="#fff" stroke-width="2" stroke-linejoin="round"/></svg>
      <span>0-800 555-01234</span>
    </div>
    <div class="contact-item" style="margin-top:12px">
      <svg width="15" height="17" viewBox="0 0 24 26"><path d="M12 24s8-8 8-14a8 8 0 0 0-16 0c0 6 8 14 8 14z" fill="none" stroke="#fff" stroke-width="2"/><circle cx="12" cy="10" r="3" fill="none" stroke="#fff" stroke-width="2"/></svg>
      <span>42 Linden Row,<br>Portland, US</span>
    </div>
    <div class="contact-item" style="margin-top:16px">
      <svg width="15" height="13" viewBox="0 0 24 20"><rect x="1" y="1" width="22" height="18" rx="2" fill="none" stroke="#fff" stroke-width="2"/><path d="M1 3l11 8 11-8" fill="none" stroke="#fff" stroke-width="2"/></svg>
      <span>customers@quellmont.example</span>
    </div>
  </div>

  <div class="foot-col touch" style="left:722px">
    <h5>Let’s Get In Touch</h5>
    <p>Nemo enim ipsam voluptatem quia voluptas sit aspernatur aut odit aut fugit, sed quia conse quuntur magni dolores eos qui ratione voluptatem sequi nesciunt. Neque porro quis quam est, qui dolorem.</p>
  </div>

  <div class="abs foot-rule"></div>
  <div class="abs copyright">Copyrights @ 2023 All Rights Reserved.</div>
</div>
</body>
</html>
```